Small boutique home based travel agency needs a flyer design and logo

I need a flyer design for my boutique home-based travel agency that specializes in designing personalized trips to Europe, ocean and river cruises and escorted small group tours to exotic destinations.

We are travel experts, provide the best customer service in the industry and would like this promoted. Open by appointment.
Would like the flyer and logo to use a globe and I like color. Please integrate photo.

Boutique

```html
<!DOCTYPE html>
<html lang="en">
<head>
<meta charset="utf-8">
<title>Meridian Voyages by Ana – Trifold Brochure</title>
<link rel="stylesheet" href="https://fonts.googleapis.com/css2?family=Arimo:wght@400;700&display=swap">
<style>
:root{
  --page-bg:#e6e9ec;
  --brand-blue:#1d5d8a;
  --brand-blue-dark:#164a6f;
  --heading-blue:#1b75bb;
  --accent-orange:#f39a1e;
  --ink:#2b2b2b;
  --paper:#ffffff;
  --sky:#8fc3e6;
  --sea:#2f8fc4;
}
*{box-sizing:border-box;margin:0;padding:0}
html,body{width:1200px;height:857px;overflow:hidden}
body{background:var(--page-bg);font-family:"Arimo",Arial,sans-serif;color:var(--ink);position:relative}
.spread{position:absolute;top:208px;width:570px;height:440px;background:var(--paper);box-shadow:0 2px 10px rgba(0,0,0,.18);overflow:hidden}
.spread--outside{left:20px}
.spread--inside{left:610px}
.spread__shapes{position:absolute;inset:0}
.block{position:absolute}
.tab{display:inline-block;background:var(--heading-blue);color:#fff;font-weight:700;font-size:11px;padding:4px 16px 4px 8px;clip-path:polygon(0 0,100% 0,92% 50%,100% 100%,0 100%)}
.tab--orange{background:var(--accent-orange)}
.item-title{color:var(--heading-blue);font-weight:700;font-size:6.6px;margin-top:9px;text-transform:uppercase}
.item-title::before{content:"● "}
.item-sub{color:var(--heading-blue);font-size:6px}
.body-text{font-size:6px;line-height:1.35;margin-top:5px}
.body-text strong{display:block}
.brand-name{font-weight:700;color:var(--heading-blue);font-size:15px;white-space:nowrap}
.brand-name--light{color:#fff;font-size:10px}
.brand-mark{display:inline-block;width:9px;height:9px;border-radius:50%;background:currentColor;margin-right:5px;vertical-align:0}
.web{font-weight:700;font-size:8.5px;letter-spacing:.3px}
.contact{color:#fff;font-size:8px;line-height:1.35}
.contact dt{font-weight:700;margin-top:7px}
.contact .contact__name{font-weight:700;font-size:8.5px}
.phone-tag{color:#fff;font-weight:700;font-size:15px}
.photo{position:absolute}
</style>
</head>
<body>

<!-- Outside spread: promotions / back panel / cover -->
<section class="spread spread--outside">
  <svg class="spread__shapes" width="570" height="440" viewBox="0 0 570 440">
    <defs>
      <linearGradient id="cruiseGrad" x1="0" y1="0" x2="0" y2="1">
        <stop offset="0" stop-color="#3a86c8"/>
        <stop offset=".45" stop-color="#9fcbe8"/>
        <stop offset=".6" stop-color="#eef3f6"/>
        <stop offset="1" stop-color="#3f6f8c"/>
      </linearGradient>
      <linearGradient id="beachGrad" x1="0" y1="0" x2="0" y2="1">
        <stop offset="0" stop-color="#7fb7e0"/>
        <stop offset=".55" stop-color="#d9ecf5"/>
        <stop offset=".75" stop-color="#36b3c9"/>
        <stop offset="1" stop-color="#1d86b0"/>
      </linearGradient>
    </defs>
    <rect x="190" y="0" width="380" height="440" fill="var(--brand-blue)"/>
    <rect x="190" y="0" width="10" height="440" fill="var(--brand-blue-dark)" opacity=".5"/>
    <rect x="380" y="0" width="190" height="315" fill="var(--paper)"/>
    <circle cx="515" cy="315" r="184" fill="var(--accent-orange)"/>
    <circle cx="515" cy="315" r="176" fill="var(--brand-blue)"/>
    <circle cx="515" cy="315" r="170" fill="url(#cruiseGrad)" role="img" aria-label="Photo of a large white cruise ship at sea"/>
    <polygon points="412,368 570,368 570,400 400,400" fill="var(--accent-orange)"/>
    <rect x="0" y="285" width="190" height="155" fill="url(#beachGrad)" role="img" aria-label="Photo of a woman in a sun hat on a tropical beach"/>
  </svg>

  <div class="block" style="left:0;top:12px;width:186px">
    <span class="tab">Promotions</span>
    <div style="padding:0 10px">
      <p class="item-title">Palmera Island Resort</p>
      <p class="item-sub">INCLUDES 3 FREE NIGHTS!</p>
      <p class="body-text">Enjoy 3 FREE Nights at the all-inclusive, remote adults only boutique Palmera Island Resort &amp; Spa. The perfect blend of lush tropical rainforest and beautiful white sand beaches. Act fast to take advantage of this amazing offer!</p>
      <p class="item-title">Rangiroa Getaway</p>
      <p class="body-text">Rangiroa Getaway Coral Bay Tahiti Resort &amp; Lagoon Crest Resort &amp; Spa</p>
      <p class="body-text">Escape to the beautiful and secluded Lagoon Crest Resort &amp; Spa on the remote island of Rangiroa with this 5-night promotion. Includes special honeymoon amenities and daily breakfast for two.</p>
      <p class="item-title">Sunstone Hotel Cancun - All Inclusive</p>
      <p class="item-sub">Milwaukee to Cancun/Riviera Maya</p>
      <p class="body-text"><strong>Deluxeview</strong>All-Inclusive - Includes all meals, beverages and more! Protect your vacation investment for just $10 per person by selecting "Best Price Guarantee"</p>
      <p class="body-text"><strong>Booking Info</strong>Save up to 45% + up to $500 resort credit</p>
    </div>
  </div>

  <div class="block" style="left:210px;top:288px;width:160px">
    <p class="brand-name brand-name--light"><span class="brand-mark"></span>Meridian Voyages</p>
    <dl class="contact" style="margin-top:10px">
      <dd class="contact__name">Meridian Voyages<br>by Ana</dd>
      <dt>(email)</dt><dd>ana@meridianvoyages.net</dd>
      <dt>(phone)</dt><dd>555-014-2290</dd>
      <dt>(web)</dt><dd>www.MeridianVoyagesbyAna.com</dd>
    </dl>
  </div>

  <div class="block" style="left:380px;top:42px;width:190px;text-align:center">
    <p class="brand-name" style="font-size:14px"><span class="brand-mark" style="color:var(--accent-orange)"></span>Meridian Voyages</p>
    <p class="brand-name" style="font-size:10px;text-align:right;padding-right:22px">by Ana</p>
    <p class="web" style="margin-top:14px">www.meridianvoyagesbyana.com</p>
  </div>

  <p class="block phone-tag" style="left:425px;top:375px">555-014-2290</p>
</section>

<!-- Inside spread: about / cruise / featured voyage -->
<section class="spread spread--inside">
  <svg class="spread__shapes" width="570" height="440" viewBox="0 0 570 440">
    <defs>
      <linearGradient id="cruisePanel" x1="0" y1="0" x2="0" y2="1">
        <stop offset="0" stop-color="#bcd5e7"/>
        <stop offset=".55" stop-color="#eef4f8"/>
        <stop offset="1" stop-color="#ffffff"/>
      </linearGradient>
      <linearGradient id="vineGrad" x1="0" y1="0" x2="0" y2="1">
        <stop offset="0" stop-color="#9cc6e3"/><stop offset=".5" stop-color="#6f9a4a"/><stop offset="1" stop-color="#4d7f9c"/>
      </linearGradient>
      <linearGradient id="hutGrad" x1="0" y1="0" x2="0" y2="1">
        <stop offset="0" stop-color="#5aa9dc"/><stop offset=".6" stop-color="#c9a873"/><stop offset="1" stop-color="#e8dcc0"/>
      </linearGradient>
      <linearGradient id="harborGrad" x1="0" y1="0" x2="0" y2="1">
        <stop offset="0" stop-color="#8cc4ea"/><stop offset=".5" stop-color="#d9a77a"/><stop offset="1" stop-color="#2b7fb3"/>
      </linearGradient>
      <linearGradient id="travelerGrad" x1="0" y1="0" x2="0" y2="1">
        <stop offset="0" stop-color="#cfe3ef"/><stop offset=".45" stop-color="#7da66a"/><stop offset="1" stop-color="#e9ecee"/>
      </linearGradient>
    </defs>
    <rect x="190" y="0" width="190" height="440" fill="url(#cruisePanel)"/>
    <rect x="0" y="270" width="380" height="155" fill="#d7e7f1"/>
    <rect x="380" y="185" width="190" height="240" fill="url(#travelerGrad)" role="img" aria-label="Photo of a smiling traveler with palm trees behind her"/>
    <circle cx="283" cy="332" r="78" fill="#d0e4f0"/>
    <circle cx="283" cy="332" r="72" fill="url(#harborGrad)" role="img" aria-label="Photo of a colourful Mediterranean harbour town"/>
    <circle cx="63" cy="354" r="72" fill="#d0e4f0"/>
    <circle cx="63" cy="354" r="66" fill="url(#vineGrad)" role="img" aria-label="Photo of a river cruise boat passing vineyards"/>
    <circle cx="178" cy="376" r="61" fill="#d0e4f0"/>
    <circle cx="178" cy="376" r="55" fill="url(#hutGrad)" role="img" aria-label="Photo of a thatched beach hut with a hammock"/>
    <rect x="0" y="425" width="570" height="15" fill="var(--heading-blue)"/>
  </svg>

  <div class="block" style="left:0;top:12px;width:186px">
    <span class="tab tab--orange">About Meridian Voyages</span>
    <div style="padding:0 10px">
      <p class="body-text" style="font-weight:700;margin-top:8px">Welcome to Meridian Voyages!</p>
      <p class="body-text" style="text-align:justify">Meridian Voyages is a full service travel agency. Our promise to our clients is to provide the best personalized customer service in the industry. We are a small agency with many years of travel experience and have the expertise to plan the travel experience that is just right for you.</p>
      <p class="body-text">We can plan your family vacation or a special trip for your group, church or club.</p>
      <p class="body-text">Meridian Voyages also plans and offers several escorted small group vacations each year to interesting and fun destinations.</p>
      <p class="body-text">To find out how we can be of service to you, please contact us and one of our agents will gladly assist you.</p>
      <p class="brand-name" style="font-size:11px;margin-top:12px;text-align:center"><span class="brand-mark" style="color:var(--accent-orange)"></span>Meridian Voyages</p>
    </div>
  </div>

  <div class="block" style="left:190px;top:12px;width:186px">
    <span class="tab tab--orange">CRUISE</span>
    <div style="padding:0 10px">
      <p class="item-title">12 Night Russia Cruise</p>
      <p class="item-sub">River Aurora</p>
      <p class="body-text">- Northway River Cruises-traveling with the best<br>- The Most Award-Winning River Cruise Line</p>
      <p class="item-title">River Cruises for Wine Lovers - Save up to $1,500</p>
      <p class="body-text">- There is nothing quite like BLUERIVER CRUISES European Wine Cruise. Discover all of the history, majesty and wonder of Europe, as you experience fairy tale castles, beautiful cathedrals and visit the famed wineries of Europe's most scenic wine regions.</p>
      <p class="body-text">- In addition to all sights, tour and dining normally included on a BlueRiver river Cruise, our wine cruises also offer these activities at no extra cost!</p>
    </div>
  </div>

  <div class="block" style="left:380px;top:12px;width:190px;padding:0 10px">
    <p class="item-title" style="margin-top:0">11 Night West Mediterranean Cruise</p>
    <p class="item-sub">Grand Meridian</p>
    <p class="body-text">For over a century and a half, the iconic ships of Harbor Line have been defining sophisticated ocean travel. They have always been The Most Famous Ocean Liners in the World.</p>
    <p class="body-text">From fabled vessels of the past to her present royal court - Grand Aurora, Grand Solstice and Grand Meridian - Harbor Line has carried guests across the great oceans and to the far points of the globe in unparalleled style. The most glamorous names of yesterday and today have made champagne toasts in her salons, waltzed the night away in her grand ballrooms and whiled away hours on her decks.</p>
    <p class="body-text">We invite you to take your place in the rich heritage of ocean travel, and write your own classic adventure tale. Join us for a journey on the legendary luxury ocean liners of Harbor Line.</p>
  </div>
</section>

</body>
</html>
```